Brochure for a paper wholesaler who wants to educate his print industry clients

We will be making a stapled informative brochure, that contains basic information about our paper products - the types of paper there is, their characteristics and other useful information.
As we are part of a paper wholesaler group in Europe - VORENT, we received a brochure in German that has this kind of information. The text in it is not as important. What is important is the layout of the document and how the text will appear in it (added in the uploaded files - 210915_Wiessenswertes_TBLK_F51.pdf).
We are allowed to tinker with this file and adjust it to our needs. So there are also .idml and .indd files available (also in the uploaded files).
We would like to keep the custom page size of 210 x290mm (8.3x11.4 in), or you can go up to 210x297mm (8.3x11.7 in).
What we want is a modern looking design that contains our companies red bordo and white/ grey colours to replace the existing green colours in this borchure. The pictures and appearance of the file can be changed according to your views and what you think would look good. We don't necessarily want to keep the same design, we just want the layout of the document be the same, as we will be placing our translated text into it. The VORENT logo should be replaced with our own logo (KUMET Logo.png).
As for how it could look, it could go together with our paper presentation, for which the design can be seen in the "KUMET Base - v2.pptx".
Holiday season, so have a lot of tasks to take care of and not as much time to check ArtHarbor as often.

```html
<!DOCTYPE html>
<html lang="en">
<head>
<meta charset="utf-8">
<title>Worth knowing! – Paper primer</title>
<link rel="stylesheet" href="https://fonts.googleapis.com/css2?family=Josefin+Sans:wght@300;400;600;700&display=swap">
<style>
  :root{
    --bordo:#86302f;
    --bordo-text:#7d2c2b;
    --grey-bg:#f1eff0;
    --grey-1:#e4e2e4;
    --grey-2:#d6d4d7;
    --paper-1:#eceaee;
    --paper-2:#dcdde6;
    --white:#ffffff;
    --text:#4a3a3a;
  }
  *{margin:0;padding:0;box-sizing:border-box}
  html,body{width:1200px;height:1000px;overflow:hidden;background:var(--grey-bg);font-family:"Josefin Sans",sans-serif}
  .canvas{position:relative;width:1200px;height:1000px}
  .spread-shapes{position:absolute;left:0;top:0}
  .page{position:absolute;top:92px;height:816px}
  .page--back{left:10px;width:588px}
  .page--front{left:600px;width:590px}

  /* contact directory */
  .directory{position:absolute;top:30px;left:69px;display:grid;grid-template-columns:120px 118px 120px 140px;column-gap:0}
  .dealer-col{display:flex;flex-direction:column}
  .dealer-badge{width:16px;height:16px;background:var(--grey-2);border-radius:3px;margin-bottom:8px}
  .dealer-badge--round{border-radius:50%}
  .dealer{font-size:7.4px;line-height:11.2px;color:var(--bordo-text);margin-bottom:14px;font-weight:400}
  .dealer b{font-weight:700}
  .dealer .gap{height:14px}

  .web{position:absolute;font-size:11px;color:var(--bordo-text);font-weight:400}
  .web--back{left:70px;top:758px}
  .web--front{right:60px;top:759px;color:var(--white)}

  .brand{position:absolute;display:flex;align-items:center;gap:22px}
  .brand-mark{width:38px;height:44px;border:2px solid currentColor}
  .brand-name{font-weight:400;letter-spacing:15px;font-size:20px}
  .brand--back{left:317px;top:738px;color:var(--white)}
  .brand--front{left:317px;top:28px;color:var(--bordo-text)}
  .brand--front .brand-mark{width:42px;height:52px}
  .brand--front .brand-name{font-size:22px;letter-spacing:17px}

  .title-block{position:absolute;left:50px;top:160px;color:var(--bordo-text)}
  .title{font-weight:700;font-size:30px;line-height:32px}
  .subtitle{font-weight:300;font-size:29px;line-height:32px;margin-top:2px}
  .tagline{font-weight:400;font-size:14px;margin-top:14px}

  .badge{position:absolute;left:435px;top:231px;width:115px;height:115px;border-radius:50%;background:var(--bordo);color:var(--white);display:flex;align-items:center;justify-content:center;text-align:center}
  .badge p{font-size:16px;line-height:19px;font-weight:600;transform:rotate(-16deg)}
</style>
</head>
<body>
<div class="canvas">
  <svg class="spread-shapes" width="1200" height="1000" viewBox="0 0 1200 1000">
    <rect x="10" y="92" width="588" height="816" fill="var(--white)"/>
    <rect x="600" y="92" width="590" height="816" fill="var(--white)"/>
    <polygon points="10,693 410,775 150,908 10,908" fill="var(--grey-1)"/>
    <polygon points="10,760 598,690 598,908 10,908" fill="var(--grey-2)" opacity=".45"/>
    <polygon points="150,908 598,680 598,908" fill="var(--bordo)"/>
    <defs>
      <linearGradient id="paperTone" x1="0" y1="0" x2="1" y2="1">
        <stop offset="0" stop-color="var(--paper-1)"/>
        <stop offset=".55" stop-color="#f4f3f6"/>
        <stop offset="1" stop-color="var(--paper-2)"/>
      </linearGradient>
    </defs>
    <polygon role="img" aria-label="Photograph of fanned white paper sheets" points="600,385 1190,345 1190,590 640,908 600,908" fill="url(#paperTone)"/>
    <polygon points="600,750 720,855 600,908" fill="var(--white)"/>
    <polygon points="630,908 1190,587 1190,908" fill="var(--bordo)"/>
  </svg>

  <section class="page page--back">
    <div class="directory">
      <div class="dealer-col">
        <span class="dealer-badge"></span>
        <p class="dealer"><b>E. BERGMANN &amp; CO.</b><br>(GmbH &amp; Co.) KG<br>Lindenhof-Ring 12<br>21465 Reinbek<br><b>T</b> +49 (0)40 5 55 10-0<br><b>F</b> +49 (0)40 5 55 10-466</p>
        <p class="dealer"><b>E. BERGMANN &amp; CO.</b><br>(GmbH &amp; Co.) KG<br>Ahornstraße 21<br>12459 Berlin<br><b>T</b> +49 (0)30 5 55 20-0<br><b>F</b> +49 (0)30 5 55 20-444</p>
        <p class="dealer"><b>E. BERGMANN &amp; CO.</b><br>(GmbH &amp; Co.) KG<br>Hafendamm 8<br>24145 Kiel<br><b>T</b> +49 (0)40 5 55 10-0<br><b>F</b> +49 (0)40 5 55 10-466</p>
        <span class="dealer-badge"></span>
        <p class="dealer"><b>NORDA</b> GmbH &amp; Co. KG<br>Großhandel<br>Weidenweg-Straße 6<br>28307 Bremen<br><b>T</b> +49 (0)4 21 55 50-0<br><b>F</b> +49 (0)4 21 55 50-200</p>
      </div>
      <div class="dealer-col">
        <span class="dealer-badge"></span>
        <p class="dealer"><b>rwt</b> GmbH &amp; Co. KG<br>Birkenstraße 4<br>30966 Hemmingen<br><b>T</b> +49 (0)5 11 55 30-0<br><b>F</b> +49 (0)5 11 55 30-290</p>
        <p class="dealer"><b>rwt</b> GmbH &amp; Co. KG<br>Kastanienallee 196<br>33609 Bielefeld<br><b>T</b> +49 (0)5 21 55 40-0<br><b>F</b>+49(0)5215554079</p>
        <span class="dealer-badge"></span>
        <p class="dealer"><b>KRAMER &amp; JENSEN</b><br>GmbH &amp; Co. KG<br>Eschenweg 215-221<br><b>50739 Köln</b><br><b>T</b> +49 (0)2 21 55 60-0<br><b>F</b> +49 (0)2 21 55 60-500</p>
        <p class="dealer"><b>KRAMER &amp; JENSEN</b><br>GmbH &amp; Co. KG<br>Ulmenstraße 50<br>44149 Dortmund<br><b>T</b> +49 (0)2 31 55 70-0<br><b>F</b> +49 (0)2 31 55 70-100</p>
        <p class="dealer"><b>KRAMER &amp; JENSEN</b><br>GmbH &amp; Co. KG<br>Gewerbegebiet Talgrund<br>Im Wiesengrund<br>54311 Trierweiler<br><b>T</b> +49 (0)6 51 5 55 80-0<br><b>F</b> +49 (0)6 51 5 55 80-10</p>
      </div>
      <div class="dealer-col">
        <span class="dealer-badge dealer-badge--round"></span>
        <p class="dealer"><b>HOLZER</b> GmbH &amp; Co. KG<br>Mühlbach-Straße 7<br>73434 Aalen/Württemberg T<br>+49 (0)73 61 5 55-0<br><b>F</b> +49 (0)73 61 5 55-170</p>
        <p class="dealer"><b>HOLZER</b> GmbH &amp; Co. KG<br>Am Steingraben 12<br>77880 Sasbach<br><b>T</b> +49 (0)78 41 55 59-0<br><b>F</b> +49 (0)78 41 55 59-344</p>
        <span class="dealer-badge"></span>
        <p class="dealer"><b>3KGmbH&amp;Co.KG</b><br>Werkstraße 24<br>85748 Garching bei München<br><b>T</b> +49 (0)89 5 55 90-0<br><b>F</b> +49 (0)89 5 55 90-100</p>
        <p class="dealer"><b>3KGmbH&amp;Co.KG</b><br>Flussstraße 28<br>90451 Nürnberg<br><b>T</b> +49 (0)9 11 55 51-0<br><b>F</b> +49 (0)9 11 55 51-222</p>
      </div>
      <div class="dealer-col">
        <span class="dealer-badge dealer-badge--round"></span>
        <p class="dealer"><b>VORENT GROSSHANDEL</b> GmbH<br>Vorent-Ring 1<br>06188 Landsberg/OT Queis<br><b>T</b> +49 (0)3 46 55 52-600<br><b>F</b> +49 (0)3 46 55 52-899</p>
        <p class="dealer"><b>VORENT GROSSHANDEL</b> GmbH<br>Lerchenfeld-Straße 3<br>64807 Dieburg<br><b>T</b> +49 (0)60 71 55 53-0<br><b>F</b> +49 (0)60 71 55 53-100</p>
        <p class="dealer"><b>VORENT GROSSHANDEL</b> GmbH<br>Auf dem Feldrain 6<br>99894 Friedrichroda/<br>OT Ernstroda<br><b>T</b> +49 (0)36 23 55 54-0<br><b>F</b> +49 (0)36 23 55 54-20</p>
        <p class="dealer"><b>VORENT GROSSHANDEL</b> GmbH<br>Waldrandweg 7<br>17209 Leizen<br>T+49(0)39922555-0<br>F+49(0)39922555-90</p>
        <p class="dealer"><b>VORENT GROSSHANDEL</b> GmbH<br>Sonnenhang-Straße 25 01458<br>Ottendorf-Okrilla<br><b>T</b> +49 (0)3 52 05 5 55-0<br><b>F</b> +49 (0)3 52 05 5 55-55</p>
      </div>
    </div>
    <p class="web web--back">www.kumet.lv</p>
    <div class="brand brand--back"><span class="brand-mark"></span><span class="brand-name">KUMET</span></div>
  </section>

  <section class="page page--front">
    <div class="brand brand--front"><span class="brand-mark"></span><span class="brand-name">KUMET</span></div>
    <div class="title-block">
      <h1 class="title">Worth knowing!</h1>
      <p class="subtitle">Formats, classes, colors, calculations</p>
      <p class="tagline">Guide for handling paper and cardboard</p>
    </div>
    <div class="badge"><p>The small<br>paper and<br>color primer</p></div>
    <p class="web web--front">www.kumet.lv</p>
  </section>
</div>
</body>
</html>
```